Prepare a modern, professional business card for Bramford Ledger Services (BLS) Our company is in the banking, compliance and finance industry. We provide kiosks, software integration, and compliance guidelines so that banks can "bank" Marijuana Dispensaries with TrevMon, Office of Halvern Affairs and NTRB approval.

Target Market(s)

Banks

Industry/Entity Type

Business

Contact Information for Business Card

Owen R Pelley
Bramford Ledger Services
Vice President
742 Quarry Ridge Road
Suite 310
Las Vegas, NV 89135
owen@bramfordls.net
702-555-0147

Font styles to use
Sans Serif

Requirements
Nice to have
• I like the clean simple appearance of Quillon computers. Perhaps the three LETTERS of BLS can be the LOGO on the Card and the Company name could be incorporated in the contact information. Like colors of white, black and gray

```html
<!DOCTYPE html>
<html lang="en">
<head>
<meta charset="utf-8">
<title>Bramford Ledger Services – Business Card</title>
<link rel="stylesheet" href="https://fonts.googleapis.com/css2?family=Open+Sans:ital,wght@0,400;0,600;0,700;0,800;1,600&display=swap">
<style>
  :root {
    --backdrop: #2f3e48;
    --card-dark: #5a5a5c;
    --card-light: #ffffff;
    --ink: #1c1c1c;
    --ink-soft: #6f6f6f;
    --logo-light: #ffffff;
    --logo-grey: #6a6a6a;
  }
  * { box-sizing: border-box; margin: 0; padding: 0; }
  html, body {
    width: 1200px;
    height: 1000px;
    overflow: hidden;
    background: var(--backdrop);
    font-family: "Open Sans", Arial, sans-serif;
  }
  .stage {
    width: 1200px;
    height: 1000px;
    display: flex;
    flex-direction: column;
    align-items: center;
    justify-content: center;
    gap: 60px;
  }
  .card {
    position: relative;
    width: 640px;
    height: 366px;
    border-radius: 4px;
    box-shadow: 0 10px 30px rgba(0,0,0,0.35);
  }
  .card--front {
    background: var(--card-dark);
    display: flex;
    align-items: center;
    justify-content: center;
  }
  .wordmark {
    font-weight: 800;
    letter-spacing: -2px;
    line-height: 1;
  }
  .card--front .wordmark {
    color: var(--logo-light);
    font-size: 110px;
    margin-top: -40px;
  }
  .card--back {
    background: var(--card-light);
    color: var(--ink);
  }
  .card--back .wordmark {
    position: absolute;
    left: 44px;
    top: 58px;
    color: var(--logo-grey);
    font-size: 72px;
  }
  .person {
    position: absolute;
    left: 382px;
    top: 48px;
  }
  .person__name {
    font-size: 19px;
    font-weight: 600;
    color: var(--ink);
  }
  .person__title {
    font-size: 17px;
    color: var(--ink-soft);
    margin-top: 2px;
  }
  .company {
    position: absolute;
    left: 30px;
    bottom: 40px;
    font-size: 21px;
    line-height: 1.5;
  }
  .company__name {
    font-weight: 600;
    font-style: italic;
  }
  .contact {
    position: absolute;
    left: 382px;
    bottom: 40px;
    font-size: 21px;
    line-height: 1.5;
  }
  .contact__label { display: inline-block; width: 28px; }
  .contact strong { font-weight: 700; }
</style>
</head>
<body>
  <main class="stage">
    <section class="card card--front" aria-label="Card front">
      <span class="wordmark">BLS</span>
    </section>

    <section class="card card--back" aria-label="Card back">
      <span class="wordmark">BLS</span>

      <div class="person">
        <p class="person__name">Owen R Pelley</p>
        <p class="person__title">Vice President</p>
      </div>

      <div class="company">
        <p class="company__name">Bramford Ledger Services</p>
        <p>742 Quarry Ridge Road Suite</p>
        <p>310 Las Vegas, NV 89135</p>
      </div>

      <div class="contact">
        <p><span class="contact__label">T</span>702-555-0147</p>
        <p>owen@bramfordls.net</p>
        <p>www.<strong>bramfordls</strong>.net</p>
      </div>
    </section>
  </main>
</body>
</html>
```